New Bottle Label for our Velmoris Grand Reserva Brandy

Graphic Design Brief
We need a new bottle label for our Brandy Gran Reserva that we want to bring to the market.
Please have a look at all our current bottles and labels and the feel of our company under www.velmoris-distill.ch. We would like the design to be still different to the rest - as it is not a whisky, not a fruit product, not a spirit like a gin, thus we need to create like a new family, but still fitting in with the rest of the products.
The bottle that we will be using for the brand is a different one than the one that we already have, the design of the bottle is attached with a document.
I have also attached a briefing in regards to Brandy in general for your information.
### 1. What is Brandy?
Brandy is a distilled spirit made from fermented wine or other fruit wines. It is traditionally aged in oak barrels, which gives it its characteristic color and rich flavor. The aging process in oak is essential for developing the aromas and quality of the brandy.
### 2. What is Brandy Reserva?
A Brandy labeled as "Reserva" has undergone a longer aging process, typically at least 2 to 3 years, in oak barrels. This aging gives the brandy a deeper, more complex flavor profile and a darker color. "Reserva" is often an indication of higher quality.
### 3. Who enjoys drinking Brandy?
Brandy is typically favored by those who appreciate a deep, rich tasting experience. This often includes older consumers who value the time-aged complexity of the spirit. However, Brandy is also gaining popularity among younger people, especially through cocktails and modern serving styles.
### 4. Why is Brandy trending?
Brandy is experiencing a resurgence as consumers increasingly value quality and artisanal production methods. Its versatility in cocktails and association with traditional, luxurious experiences have also contributed to its renewed popularity.
### 5. What colors would be associated with Brandy?
The typical colors associated with Brandy are warm gold, amber, and deep golden-brown tones. These colors reflect the aging process in oak barrels and the richness of the flavors. Other associated colors might include dark brown and mahogany.
### 6. What is important to customers when buying Brandy?
Customers care about the origin of the Brandy, the aging time, the quality of the ingredients, the production method, and the brand. They also pay attention to the prestige of the product and the authenticity of the production.
### 7. What is not important to customers when buying Brandy?
For many customers, the price and packaging (unless it’s especially exclusive) may be less important than the quality and taste of the Brandy. The distillery name might be less significant if it isn’t tied to a particular reputation.
### 8. What do customers know about Swiss Brandy?
Swiss Brandy is still relatively unknown in many markets, but customers who are familiar with it appreciate the precision and quality of Swiss production. Swiss Brandy is assumed to be made with care and under strict quality standards.
### 9. What is Brandy Gran Reserva?
**Brandy Gran Reserva** is an even higher quality and longer-aged version of Brandy. Generally, a Gran Reserva is aged for at least 5 to 10 years or more in oak barrels. This extended aging process gives the Brandy an especially deep, complex flavor profile and often a darker, richer color. Gran Reserva is often regarded as the top-tier product within a Brandy range and appeals to discerning consumers who value quality, refinement, and a luxurious tasting experience.
The label “Gran Reserva” thus indicates the highest quality level for Brandies, similar to other spirits (like wine or whisky), where the aging time is a critical factor.
We age our Brandy Gran Reserva in the Solara way.
### 10. What emotions are associated with Brandy?
Brandy is often associated with luxury, relaxation, and comfort. It evokes feelings of tradition, elegance, and sophistication. Drinking Brandy is frequently seen as a moment of reflection and enjoyment.
### 11. How should Brandy be marketed?
Brandy should be marketed with a focus on its artisanal production, quality, and tradition. A narrative around the product, its aging, and origin can help create an emotional connection with the customer. The marketing should also emphasize the versatility of Brandy, whether consumed neat or in cocktails.
**Label design**:
The label should reflect the exclusivity of the product, with an elegant, minimalist design. The label should include information about the aging time, the use of oak barrels, and a brief story about the Brandy’s production.
we would like to have a modern look to the whole deisgn of the brandy
Customers that like Brandy
Switzerland
Distillery

```html
<!DOCTYPE html>
<html lang="en">
<head>
<meta charset="utf-8">
<title>Velmoris Grand Reserva Brandy – Bottle Label</title>
<link rel="stylesheet" href="https://fonts.googleapis.com/css2?family=Roboto+Slab:wght@700&family=Roboto:wght@400;500;900&display=swap">
<style>
  :root {
    --page: #ffffff;
    --label-black: #050505;
    --gold-light: #f6e39a;
    --gold-mid: #c99a3e;
    --gold-deep: #7d5a1c;
    --gold-text: #d4ad55;
    --barrel-dark: #1a1a1a;
  }
  html, body {
    margin: 0;
    padding: 0;
    width: 831px;
    height: 1200px;
    overflow: hidden;
    background: var(--page);
  }
  .canvas {
    position: relative;
    width: 831px;
    height: 1200px;
  }
  .label {
    position: absolute;
    left: 0;
    top: 0;
    width: 831px;
    height: 1200px;
  }
  .brand-name {
    font-family: "Roboto Slab", serif;
    font-weight: 700;
    font-size: 54px;
    fill: var(--gold-text);
  }
  .distillery {
    font-family: "Roboto Slab", serif;
    font-weight: 700;
    font-size: 25px;
    letter-spacing: 1px;
    fill: var(--gold-text);
  }
  .grade {
    font-family: "Roboto", sans-serif;
    font-weight: 500;
    font-size: 23px;
    letter-spacing: 19px;
    fill: var(--gold-text);
  }
  .product {
    font-family: "Roboto", sans-serif;
    font-weight: 900;
    font-size: 122px;
    letter-spacing: 2px;
  }
  .age-number {
    font-family: "Roboto", sans-serif;
    font-weight: 900;
    font-size: 56px;
    fill: var(--gold-light);
  }
  .age-unit {
    font-family: "Roboto", sans-serif;
    font-weight: 500;
    font-size: 13px;
    letter-spacing: 7px;
    fill: var(--label-black);
  }
</style>
</head>
<body>
<main class="canvas">
  <svg class="label" viewBox="0 0 831 1200" xmlns="http://www.w3.org/2000/svg">
    <defs>
      <linearGradient id="goldRim" x1="0" y1="0" x2="1" y2="1">
        <stop offset="0" stop-color="var(--gold-deep)"/>
        <stop offset="0.3" stop-color="var(--gold-light)"/>
        <stop offset="0.6" stop-color="var(--gold-mid)"/>
        <stop offset="1" stop-color="var(--gold-deep)"/>
      </linearGradient>
      <linearGradient id="goldType" x1="0" y1="0" x2="1" y2="0">
        <stop offset="0" stop-color="var(--gold-light)"/>
        <stop offset="0.45" stop-color="var(--gold-mid)"/>
        <stop offset="0.75" stop-color="var(--gold-deep)"/>
        <stop offset="1" stop-color="var(--gold-mid)"/>
      </linearGradient>
      <radialGradient id="barrelTone" cx="0.5" cy="0.4" r="0.6">
        <stop offset="0" stop-color="#2c2c2c"/>
        <stop offset="1" stop-color="var(--barrel-dark)"/>
      </radialGradient>
      <radialGradient id="glowTop" cx="0.5" cy="0" r="0.7">
        <stop offset="0" stop-color="var(--gold-mid)" stop-opacity="0.22"/>
        <stop offset="1" stop-color="var(--gold-mid)" stop-opacity="0"/>
      </radialGradient>
    </defs>

    <!-- label body -->
    <rect class="label-rim" x="145" y="150" width="541" height="900" rx="270" fill="url(#goldRim)"/>
    <rect class="label-field" x="157" y="162" width="517" height="876" rx="258" fill="var(--label-black)"/>

    <!-- inner frame band -->
    <g class="inner-frame" role="img" aria-label="Gold hatched decorative frame band">
      <rect x="175" y="180" width="481" height="840" rx="240" fill="none" stroke="var(--gold-mid)" stroke-width="2"/>
      <rect x="186" y="191" width="459" height="818" rx="229" fill="none" stroke="var(--gold-mid)" stroke-opacity="0.55" stroke-width="18"/>
      <rect x="198" y="203" width="435" height="794" rx="217" fill="none" stroke="var(--gold-mid)" stroke-width="2"/>
    </g>
    <!-- frame opening behind the title -->
    <rect class="frame-gap" x="170" y="485" width="36" height="215" fill="var(--label-black)"/>
    <rect class="frame-gap" x="625" y="485" width="36" height="215" fill="var(--label-black)"/>

    <rect class="top-glow" x="205" y="205" width="421" height="200" rx="200" fill="url(#glowTop)"
          role="img" aria-label="Soft golden sunburst glow"/>

    <!-- brand -->
    <text class="brand-name" x="415.5" y="378" text-anchor="middle">Velmoris</text>
    <text class="distillery" x="415.5" y="423" text-anchor="middle">SWISS</text>
    <text class="distillery" x="415.5" y="455" text-anchor="middle">DISTILLERY</text>

    <!-- product -->
    <text class="grade" x="425" y="546" text-anchor="middle">GRANDRESERVA</text>
    <text class="product" x="415.5" y="666" text-anchor="middle" fill="url(#goldType)">BRANDY</text>

    <!-- barrel illustration area with age seal -->
    <path class="barrel-art" d="M345 700 h140 a40 40 0 0 1 40 40 v50 a45 45 0 0 1 25 45 v40 a30 30 0 0 1 -30 30 h-210 a30 30 0 0 1 -30 -30 v-40 a45 45 0 0 1 25 -45 v-50 a40 40 0 0 1 40 -40 z"
          fill="url(#barrelTone)" role="img" aria-label="Stacked oak barrels illustration"/>
    <g class="age-seal">
      <circle cx="415.5" cy="850" r="32" fill="none" stroke="var(--gold-mid)" stroke-width="3"/>
      <text class="age-number" x="415.5" y="870" text-anchor="middle">8</text>
      <rect x="363" y="872" width="105" height="20" fill="var(--gold-mid)"/>
      <text class="age-unit" x="419" y="887" text-anchor="middle">YEARS</text>
    </g>
  </svg>
</main>
</body>
</html>
```